Kettlelanternpress: Self-help book needs Promotional Postcard

Need a postcard 8.5" x 5.5" to promote my upcoming book. Its a self-help career book for women focusing on how the mother-daughter relationship impacts careers and tips and solutions for success. The model includes 5 different types of daughters.
Title: Where Did the Quiet Garden Lead Us?
Breathe new life into your career by understanding your mother daughter relationship.
Book release is January 9, 2017
Updates

I just uploaded 5 images of the daughter types without the words, better to use these, thanks! Added Thursday, December 29, 2016

Target Market(s)

This book is targeted towards women

Industry/Entity Type

Promotional

Font styles to use
Serif
Other font styles liked:
• see website text

Colors
00a990
ec252d
e34297

Requirements
Must have
• Eye catching promotional postcard. Must have image of book on front with title and subtitle, author name and website. I'd like images of the 5 daughters on the front.
• Colors should match the cover green and pink
• Back can have quotes and author bio
• can look at website (not quite completed) for more inspiration www.kettlelanternpress.example
Nice to have
• Curious to see how the postcard compliments the book and website.

```html
<!DOCTYPE html>
<html lang="en">
<head>
<meta charset="utf-8">
<title>Where Did the Quiet Garden Lead Us? — Postcard</title>
<link rel="stylesheet" href="https://fonts.googleapis.com/css2?family=Fira+Sans:wght@400;600;700&family=Merriweather:ital,wght@0,400;0,700;1,400&display=swap">
<style>
  :root{
    --pink:#b0306a;
    --pink-bright:#e34297;
    --pink-deep:#8c2252;
    --green:#4f6b3c;
    --green-dark:#3c5430;
    --charcoal:#3b3a39;
    --charcoal-dark:#2c2b2a;
    --white:#ffffff;
    --cream:#f3efe6;
    --page:#ffffff;
  }
  *{box-sizing:border-box;margin:0;padding:0}
  html,body{width:889px;height:1200px;overflow:hidden;background:var(--page)}
  body{position:relative;font-family:"Fira Sans",sans-serif;color:var(--white)}

  .card{position:absolute;left:0;width:889px;height:590px;overflow:hidden}
  .card--front{top:0;background:linear-gradient(180deg,var(--charcoal) 0%,var(--charcoal-dark) 100%)}
  .card--back{top:610px;background:var(--green)}

  /* front */
  .front-band{position:absolute;left:0;top:18px;width:889px;height:92px;background:var(--pink)}
  .front-title{position:absolute;left:26px;top:26px;font-weight:700;font-size:27px;letter-spacing:.2px}
  .front-subtitle{position:absolute;left:26px;top:64px;font-size:15px;font-style:italic;font-family:"Merriweather",serif;color:var(--cream)}
  .book-cover{position:absolute;left:80px;top:130px;width:300px;height:330px;
    background:linear-gradient(160deg,#f2ece0 0%,#d9cfc0 100%);box-shadow:6px 8px 18px rgba(0,0,0,.5)}
  .daughters{position:absolute;left:410px;top:120px;width:465px}
  .daughter{position:relative;height:70px;margin-bottom:2px;background:var(--pink);display:flex;align-items:center}
  .daughter:nth-child(even){background:var(--pink-deep)}
  .daughter__figure{width:56px;height:62px;margin:0 12px;border-radius:28px 28px 4px 4px;
    background:linear-gradient(180deg,#ffffff 0%,#e7d3dc 100%)}
  .daughter__quote{flex:1;font-family:"Merriweather",serif;font-style:italic;font-size:14px;line-height:1.3}
  .daughter__name{display:block;font-style:normal;font-size:12px;color:var(--cream);margin-top:2px}
  .front-cta{position:absolute;left:0;top:488px;width:889px;text-align:center}
  .front-cta__lead{font-size:15px;font-weight:600;letter-spacing:1px;text-transform:uppercase}
  .front-cta__url{font-size:40px;font-weight:700;margin-top:4px}

  /* back */
  .back-band{position:absolute;left:0;top:14px;width:889px;height:50px;background:var(--pink)}
  .back-title{position:absolute;left:26px;top:22px;font-size:26px;font-weight:700}
  .back-intro{position:absolute;left:26px;top:82px;width:410px;font-size:12.5px;line-height:1.45}
  .review{margin-top:12px;font-family:"Merriweather",serif;font-style:italic;font-size:11.5px;line-height:1.45}
  .review__by{display:block;font-family:"Fira Sans",sans-serif;font-style:normal;font-weight:700;font-size:11.5px;margin-top:3px}
  .review__role{display:block;font-family:"Fira Sans",sans-serif;font-style:normal;font-size:10.5px;text-transform:uppercase;letter-spacing:.5px}
  .author-photo{position:absolute;left:460px;top:82px;width:160px;height:196px;border:4px solid var(--white);
    background:linear-gradient(160deg,#a39482 0%,#5e5043 100%)}
  .speaking{position:absolute;left:640px;top:86px;width:230px;font-size:30px;font-weight:700;line-height:1.15;color:var(--pink-bright)}
  .speaking{background:var(--pink);color:var(--white);padding:14px 16px}
  .bio{position:absolute;left:640px;top:300px;width:232px;font-size:12px;line-height:1.45}
  .bio strong{font-weight:700}
  .back-footer{position:absolute;left:0;top:520px;width:889px;height:56px;background:var(--pink);display:flex;align-items:center;padding:0 24px}
  .social{display:flex;gap:8px;margin-right:30px}
  .social span{width:26px;height:26px;border-radius:50%;background:var(--green-dark)}
  .back-footer__text{font-size:27px;font-weight:600}
</style>
</head>
<body>

<section class="card card--front">
  <div class="front-band"></div>
  <h1 class="front-title">Where Did the Quiet Garden Lead Us?</h1>
  <p class="front-subtitle">Breathe new life into your career by understanding your mother daughter relationship.</p>

  <div class="book-cover" role="img" aria-label="Book cover of Where Did the Quiet Garden Lead Us? by Maren Holloway Price, M.A., M.Ed."></div>

  <div class="daughters">
    <div class="daughter"><div class="daughter__figure" role="img" aria-label="Silhouette of a woman, daughter type one"></div><p class="daughter__quote">"It's everyone else, not me!"<span class="daughter__name">-Willow Wren</span></p></div>
    <div class="daughter"><div class="daughter__figure" role="img" aria-label="Silhouette of a woman, daughter type two"></div><p class="daughter__quote">"Don't tell me what to do."<span class="daughter__name">-Rebel Rosa</span></p></div>
    <div class="daughter"><div class="daughter__figure" role="img" aria-label="Silhouette of a woman, daughter type three"></div><p class="daughter__quote">"Sometimes I feel like an imposter."<span class="daughter__name">-Firefly Fiona</span></p></div>
    <div class="daughter"><div class="daughter__figure" role="img" aria-label="Silhouette of a woman, daughter type four"></div><p class="daughter__quote">"The apple doesn't fall far from the tree, or does it?"<span class="daughter__name">-Echo Ella</span></p></div>
    <div class="daughter"><div class="daughter__figure" role="img" aria-label="Silhouette of a woman, daughter type five"></div><p class="daughter__quote">"I like the weight of the world on my shoulders."<span class="daughter__name">-Homing Hana</span></p></div>
  </div>

  <div class="front-cta">
    <p class="front-cta__lead">For more information please visit</p>
    <p class="front-cta__url">www.kettlelanternpress.example</p>
  </div>
</section>

<section class="card card--back">
  <div class="back-band"></div>
  <h2 class="back-title">Where Did the Quiet Garden Lead Us?</h2>

  <div class="back-intro">
    <p>Are you unhappy at work? Feeling uncertain about your career choices or growth? Your relationship with your mother might be the starting point you need for a more satisfying future in your career and life. Unlock the mystery of the patterns and choices you make throughout your career. Read about the five daughter types, and learn how to propel your career forward.</p>
    <p class="review">"A fresh and honest look at the ties that shape our working lives. Every woman who has wondered why she keeps repeating the same career choices will find clarity, comfort and practical tools here."
      <span class="review__by">Jonah Pereira-Whitcombe, PhD</span>
      <span class="review__role">Host of a syndicated radio program</span></p>
    <p class="review">"Warm, wise and useful. This book turns family history into a map for growth at work."
      <span class="review__by">Dr. Odette Pennwick</span>
      <span class="review__role">Author, coach and leadership speaker</span></p>
  </div>

  <div class="author-photo" role="img" aria-label="Portrait photograph of the author"></div>
  <p class="speaking">Book Maren for a Speaking Event!</p>

  <p class="bio"><strong>Maren Holloway Price, M.A., M.Ed.</strong> is a clinical career counselor and licensed mental health counselor who has been helping clients make meaningful career transitions and address workplace challenges for over 20 years. She is the recipient of a national counseling award and a frequent speaker. Her model of daughter types offers a fresh look at how the adult mother-daughter relationship shapes work.</p>

  <div class="back-footer">
    <div class="social" aria-hidden="true"><span></span><span></span><span></span><span></span></div>
    <p class="back-footer__text">For more information visit www.kettlelanternpress.example</p>
  </div>
</section>

</body>
</html>
```